Civic Holdwell Business Card

We are looking to design new business cards for our company. We have two office locations and would like to have both full addresses on the card. Each address needs two lines for the building name and street address and a line or two for the city, state and zip code. There should be a place for 2-3 phone numbers. The addresses and phone numbers are at the bottom of this description. We also need a place to put our company website and one email address. Our logo is attached.
We would like the card to be two sided. The back of the card should have a blue background with some part of our logo design on it. We would like the full logo on the front of the card as well. The front of the card should have a white background with the blue logo. We are open to listing our addresses on the front or the back of the card. The person who designed our logo gave us an excellent business card idea that we really liked. I have attached a picture of his business card idea so that we can build off of it.
Addresses:
The Tanner Hall
2184 17th Street NW
Washington, DC 20007
Marlow Crest Tower
410 Dorsen Avenue #2215
Miami, FL 33131
Phone Numbers: (202) 555-0148
(202) 555-0193
Website: www.civicholdwell.example

```html
<!DOCTYPE html>
<html lang="en">
<head>
<meta charset="utf-8">
<title>Civic Holdwell Business Card</title>
<link rel="stylesheet" href="https://fonts.googleapis.com/css2?family=Questrial&display=swap">
<style>
  :root {
    --page: #e9e9ec;
    --card-white: #ffffff;
    --ink: #1e2470;
    --rule: #3a44a8;
    --navy-deep: #16165e;
    --navy-mid: #24268a;
    --navy-glow: #4558aa;
    --on-navy: #ffffff;
  }
  * { box-sizing: border-box; margin: 0; padding: 0; }
  html, body {
    width: 1200px; height: 1200px; overflow: hidden;
    background: var(--page);
    font-family: "Questrial", "Century Gothic", sans-serif;
  }
  .canvas {
    width: 1200px; height: 1200px;
    display: flex; flex-direction: column; align-items: center;
    justify-content: center; gap: 60px;
  }
  .card {
    width: 900px; height: 514px; position: relative;
    box-shadow: 0 6px 24px rgba(20, 20, 60, 0.18);
  }
  /* Front: addresses + logo */
  .card-front { background: var(--card-white); color: var(--ink); }
  .addresses {
    position: absolute; left: 70px; top: 88px;
    font-size: 23px; line-height: 1.42; letter-spacing: 0.3px;
  }
  .office + .office { margin-top: 30px; }
  .phones { margin-top: 24px; font-weight: 700; letter-spacing: 0.6px; }
  .divider {
    position: absolute; left: 450px; top: 70px; width: 2px; height: 334px;
    background: var(--rule);
  }
  .brand {
    position: absolute; display: flex; align-items: center; gap: 14px;
  }
  .brand-square { flex: none; border-radius: 4px; }
  .brand-name { text-transform: uppercase; white-space: nowrap; line-height: 1; }
  .card-front .brand { left: 494px; top: 200px; }
  .card-front .brand-square { width: 46px; height: 46px; background: var(--ink); }
  .card-front .brand-name { font-size: 40px; letter-spacing: 1px; color: var(--ink); }
  /* Back: blue with logo */
  .card-back {
    background: radial-gradient(ellipse 62% 70% at 50% 42%, var(--navy-glow) 0%, var(--navy-mid) 55%, var(--navy-deep) 100%);
    color: var(--on-navy); overflow: hidden;
  }
  .card-back .brand { left: 50%; top: 200px; transform: translateX(-50%); gap: 18px; }
  .card-back .brand-square { width: 72px; height: 72px; background: var(--on-navy); }
  .card-back .brand-name { font-size: 60px; letter-spacing: 2px; color: var(--on-navy); }
  .swoosh { position: absolute; left: 190px; top: 272px; }
  .website {
    position: absolute; left: 0; right: 0; bottom: 52px; text-align: center;
    font-size: 24px; letter-spacing: 0.8px; text-transform: uppercase;
  }
</style>
</head>
<body>
<main class="canvas">
  <section class="card card-front">
    <div class="addresses">
      <address class="office" style="font-style:normal">
        The Tanner Hall<br>2184 17th Street NW<br>Washington<br>DC 20007
      </address>
      <address class="office" style="font-style:normal">
        Marlow Crest Tower<br>410 Dorsen Avenue #2215<br>Miami<br>FL 33131
      </address>
      <p class="phones">Phone-(202) 555-0148 , (202) 555-0193</p>
    </div>
    <div class="divider"></div>
    <div class="brand">
      <span class="brand-square"></span>
      <span class="brand-name">Civic Holdwell</span>
    </div>
  </section>

  <section class="card card-back">
    <svg class="swoosh" width="520" height="60" viewBox="0 0 520 60" aria-hidden="true">
      <defs>
        <linearGradient id="swooshFade" x1="0" x2="1">
          <stop offset="0" stop-color="#ffffff" stop-opacity="0"/>
          <stop offset="0.5" stop-color="#ffffff" stop-opacity="0.35"/>
          <stop offset="1" stop-color="#ffffff" stop-opacity="0"/>
        </linearGradient>
      </defs>
      <path d="M0 52 Q260 -4 520 18 Q260 10 0 52 Z" fill="url(#swooshFade)"/>
    </svg>
    <div class="brand">
      <span class="brand-square"></span>
      <span class="brand-name">Civic Holdwell</span>
    </div>
    <p class="website">www.civicholdwell.example</p>
  </section>
</main>
</body>
</html>
```